Boutique custom software development company needs new business card

Our nearly 20 year old custom software development company would like to better include the fact that we are now providing Bitcoin services. These new services are B2B include education (how to acquire and securely hold Bitcoin) and integrating Bitcoin payments into existing ecommerce sites or other existing systems. Please keep the card clean and simple. Attached is our current design and some other files. vexalon.example

Target Market(s)

businesses owners interested in long term relationship

Industry/Entity Type

Custom software development and Bitcoin

Contact Information for Business Card

Marcus Ellwood, marcus@vexalon.example, vexalon.example, (888) 555-VEXAL

Font styles to use
Other font styles liked:
• monospace

Requirements
Must have
• double-sided
Nice to have
• clean and simple
Should not have
• physical address

```html
<!DOCTYPE html>
<html lang="en">
<head>
<meta charset="UTF-8">
<title>Vexalon Business Card</title>
<link rel="stylesheet" href="https://fonts.googleapis.com/css2?family=Jost:wght@400;500;600;700&family=Courier+Prime:wght@700&display=swap">
<style>
  :root {
    --blue: #3a72b8;
    --orange: #e8761f;
    --ink: #333333;
    --paper: #ffffff;
    --paper-shade: #ececec;
    --backdrop: #2e2f31;
  }
  * { margin: 0; padding: 0; box-sizing: border-box; }
  html, body {
    width: 1200px; height: 900px; overflow: hidden;
    background: var(--backdrop);
    font-family: "Jost", sans-serif;
  }
  .canvas { position: relative; width: 1200px; height: 900px; }
  .card {
    position: absolute; left: 250px; width: 700px; height: 400px;
    background: linear-gradient(110deg, var(--paper-shade) 0%, var(--paper) 70%);
    overflow: hidden;
    box-shadow: 0 12px 30px rgba(0,0,0,0.45);
  }
  .card--front { top: 35px; }
  .card--back { top: 465px; }
  .card__bands { position: absolute; inset: 0; width: 100%; height: 100%; }

  /* Front side */
  .brand-mark {
    position: absolute; left: 430px; top: 48px;
    width: 150px; height: 150px; background: var(--blue);
  }
  .brand-domain {
    position: absolute; right: 40px; top: 222px;
    font-family: "Courier Prime", monospace; font-weight: 700;
    font-size: 30px; color: var(--ink); letter-spacing: 1px;
  }
  .web-address {
    position: absolute; color: var(--paper);
    font-size: 17px; letter-spacing: 1.5px; font-weight: 400;
  }
  .card--front .web-address { left: 34px; bottom: 16px; }
  .card--back .web-address { right: 30px; bottom: 36px; }

  /* Back side */
  .wordmark {
    position: absolute; left: 300px; top: 40px;
    font-size: 70px; font-weight: 700; line-height: 1;
    color: var(--blue); letter-spacing: -1px;
  }
  .tagline {
    position: absolute; left: 304px; top: 116px;
    font-size: 24px; font-weight: 400; color: var(--blue); letter-spacing: -0.3px;
  }
  .services {
    position: absolute; left: 304px; top: 154px;
    font-size: 17px; font-weight: 500; color: var(--orange); letter-spacing: 0.2px;
  }
  .holder-name {
    position: absolute; left: 40px; top: 268px;
    font-size: 24px; font-weight: 600; color: var(--orange); letter-spacing: 0.5px;
  }
  .name-rule {
    position: absolute; left: 282px; right: 40px; top: 286px;
    height: 1px; background: var(--orange);
  }
  .contact-list { position: absolute; left: 40px; top: 312px; list-style: none; }
  .contact-list li {
    display: flex; align-items: center; gap: 10px;
    font-size: 18px; color: var(--ink); margin-bottom: 6px;
  }
  .contact-list svg { width: 18px; height: 18px; fill: var(--blue); }
</style>
</head>
<body>
<main class="canvas">
  <section class="card card--front" aria-label="Card front">
    <svg class="card__bands" viewBox="0 0 700 400" aria-hidden="true">
      <polygon points="0,338 240,338 310,387 310,400 0,400" fill="var(--orange)"/>
      <rect x="300" y="387" width="400" height="13" fill="var(--blue)"/>
    </svg>
    <div class="brand-mark" aria-hidden="true"></div>
    <div class="brand-domain">vexalon.example</div>
    <div class="web-address">www.vexalon.example</div>
  </section>

  <section class="card card--back" aria-label="Card back">
    <svg class="card__bands" viewBox="0 0 700 400" aria-hidden="true">
      <rect x="0" y="386" width="430" height="14" fill="var(--blue)"/>
      <rect x="430" y="312" width="270" height="88" fill="var(--orange)"/>
    </svg>
    <div class="wordmark">VEXALON</div>
    <div class="tagline">developer of custom applications</div>
    <div class="services">Bitcoin payments &amp; education for business</div>
    <div class="holder-name">MARCUS ELLWOOD</div>
    <div class="name-rule"></div>
    <ul class="contact-list">
      <li>
        <svg viewBox="0 0 24 24" aria-hidden="true"><path d="M6.6 10.8a15.1 15.1 0 0 0 6.6 6.6l2.2-2.2a1 1 0 0 1 1-.25 11.4 11.4 0 0 0 3.6.57 1 1 0 0 1 1 1V20a1 1 0 0 1-1 1A17 17 0 0 1 3 4a1 1 0 0 1 1-1h3.5a1 1 0 0 1 1 1c0 1.25.2 2.45.57 3.57a1 1 0 0 1-.25 1z"/></svg>
        (888) 555-VEXAL
      </li>
      <li>
        <svg viewBox="0 0 24 24" aria-hidden="true"><path d="M3 5h18a1 1 0 0 1 1 1v12a1 1 0 0 1-1 1H3a1 1 0 0 1-1-1V6a1 1 0 0 1 1-1zm9 7.5L4 7.5V9l8 5 8-5V7.5z"/></svg>
        marcus@vexalon.example
      </li>
    </ul>
    <div class="web-address">www.vexalon.example</div>
  </section>
</main>
</body>
</html>
```